Business Card for Quillmark Ledger - A cannabis publication for executives.

I'd like some business cards for Quillmark Ledger. The logo is done (great job!) and I need a card design I will use with PRINTLY. I made it a short project to allow time for printing before an event. These will be standard sized cards (final artwork size 3.66" x 2.16" at 300dpi) with a final card size of 3.5" x 2.0". (See PRINTLY.com if you need more info.) I might try rounded corners but am not sure yet. I think the design will work okay with rounded.

Quillmark Ledger will be a bi-weekly publication for the cannabis industry. It is targeted to investors and industry executives, not consumers or pot smokers. So our market is more B2B. However I am open to creativity and making the card something people remark on.

My contact for card:

Dana Merrow
Founder/CEO
dana@quillmarkledger.example

2740 Harlow Avenue
Boston MA 02135
(617)555-0194

Target Market(s)

Executives, Industry people and investors in the Cannabis sector.

Contact Information for Business Card

PRINTLY does do double sided and the second side can be the same or different images. Only one side is required but use of the second side would be a bonus.

Font styles to use
Serif
Sans Serif
Decorative

Colors

Designer to choose colors to be used in the design.

Requirements
Must have
• Logo, contact info
Nice to have
• Style and design to make the card stand out in a crowd.

```html
<!DOCTYPE html>
<html lang="en">
<head>
<meta charset="utf-8">
<title>Quillmark Ledger — Business Card</title>
<link rel="stylesheet" href="https://fonts.googleapis.com/css2?family=Montserrat:wght@400;500;600&display=swap">
<style>
  :root {
    --canvas: #f2f2f0;
    --card: #0b0b0b;
    --brand-blue: #1e73be;
    --brand-green: #7cb82f;
    --ink-light: #f4f4f4;
    --ink-muted: #d9d9d9;
  }
  * { box-sizing: border-box; margin: 0; padding: 0; }
  html, body {
    width: 1200px; height: 1200px; overflow: hidden;
    background: var(--canvas);
    font-family: "Montserrat", sans-serif;
  }
  .sheet {
    width: 1200px; height: 1200px;
    display: flex; flex-direction: column;
    align-items: center; justify-content: center; gap: 60px;
  }
  .card {
    position: relative;
    width: 900px; height: 514px;
    background: var(--card);
    border-radius: 4px;
    overflow: hidden;
    box-shadow: 0 10px 28px rgba(0,0,0,.22);
  }
  .card__edge {
    position: absolute; top: 0; left: 0; right: 0; height: 8px;
    background: linear-gradient(to right, var(--brand-blue) 0 30%, var(--brand-green) 30% 100%);
  }
  .card__edge--bottom { top: auto; bottom: 0; opacity: .0; }

  /* Contact side */
  .contact {
    position: absolute; inset: 0;
    display: flex; flex-direction: column; align-items: center;
    padding-top: 120px;
    color: var(--ink-light);
  }
  .contact__name { font-size: 50px; font-weight: 500; letter-spacing: .5px; }
  .contact__title { font-size: 22px; font-weight: 600; margin-top: 6px; }
  .contact__list { margin-top: 40px; list-style: none; display: flex; flex-direction: column; gap: 18px; }
  .contact__item { display: flex; align-items: flex-start; gap: 18px; font-size: 18px; line-height: 1.45; color: var(--ink-muted); }
  .contact__icon { flex: none; width: 40px; height: 40px; }

  /* Brand side */
  .brand {
    position: absolute; inset: 0;
    display: flex; align-items: center; justify-content: center; gap: 22px;
  }
  .brand__mark { width: 44px; height: 44px; background: var(--brand-green); }
  .brand__name { font-size: 64px; font-weight: 600; color: var(--brand-blue); letter-spacing: .5px; }
</style>
</head>
<body>
<main class="sheet">
  <section class="card card--contact" aria-label="Card back with contact details">
    <div class="card__edge"></div>
    <div class="contact">
      <h1 class="contact__name">Dana Merrow</h1>
      <p class="contact__title">Founder/CEO</p>
      <ul class="contact__list">
        <li class="contact__item">
          <svg class="contact__icon" viewBox="0 0 40 40" aria-hidden="true">
            <circle cx="20" cy="20" r="18" fill="none" stroke="#f4f4f4" stroke-width="1.6"/>
            <rect x="11" y="14" width="18" height="12" fill="none" stroke="#f4f4f4" stroke-width="1.6"/>
            <path d="M11 14 L20 21 L29 14" fill="none" stroke="#f4f4f4" stroke-width="1.6"/>
          </svg>
          <span style="padding-top:8px">dana@quillmarkledger.example</span>
        </li>
        <li class="contact__item">
          <svg class="contact__icon" viewBox="0 0 40 40" aria-hidden="true">
            <circle cx="20" cy="20" r="18" fill="none" stroke="#f4f4f4" stroke-width="1.6"/>
            <path d="M20 29 C15 23 13 20 13 17 A7 7 0 0 1 27 17 C27 20 25 23 20 29 Z" fill="none" stroke="#f4f4f4" stroke-width="1.6"/>
            <circle cx="20" cy="17" r="2.5" fill="none" stroke="#f4f4f4" stroke-width="1.6"/>
          </svg>
          <span style="padding-top:8px">2740 Harlow Avenue<br>Boston MA 02135<br>(617)555-0194</span>
        </li>
      </ul>
    </div>
  </section>

  <section class="card card--brand" aria-label="Card front with company name">
    <div class="card__edge"></div>
    <div class="brand">
      <span class="brand__mark" aria-hidden="true"></span>
      <span class="brand__name">Quillmark Ledger</span>
    </div>
  </section>
</main>
</body>
</html>
```